Billboard design for dentist that sees only children

I own a 12' x 25' digital billboard and I need help with billboard design. My wife is a general dentist that only sees children and is very passionate about giving them a quality dental experience . She has a great reputation in town. Obviously with a billboard there can't be a lot of reading. Maybe something that shows safety, love, experience and children. I am completely open to your ideas. In addition I have other businesses that also need billboard design so this could lead to more work. If you go to Maplecovedental.com under the about section you will find more information about the practice and our phone number. Attached is our logo which could be changed and content specs for the digital billboard. Happy Designing!!

Target Market(s)

Parents with children

Colors

Designer to choose colors to be used in the design.

Requirements
Must have
• Must attract attention and be nice to look at.
Nice to have
• Probably should have children in the picture ..... Maybe
Should not have
• If I see something I don't like I will let you know

```html
<!DOCTYPE html>
<html lang="en">
<head>
<meta charset="utf-8">
<title>Maple Cove Dental – Billboard Presentation</title>
<link rel="stylesheet" href="https://fonts.googleapis.com/css2?family=Montserrat:wght@400;500;600;700&family=Jost:wght@400;500&display=swap">
<style>
  :root {
    --stage-dark: #383838;
    --stage-title: #cfcfcf;
    --sheet-white: #ffffff;
    --headline-blue: #3c63a8;
    --headline-navy: #1f3f6f;
    --phone-teal: #1f5a50;
    --brand-teal: #2a7a6a;
    --brand-blue: #3a7fc0;
    --body-grey: #333333;
    --spec-blue: #2b5292;
    --spec-grey: #4a4a4a;
    --rule: #333333;
  }
  * { margin: 0; padding: 0; box-sizing: border-box; }
  html, body { width: 1200px; height: 1094px; overflow: hidden; background: var(--sheet-white); }
  body { position: relative; font-family: "Montserrat", sans-serif; }

  .stage { position: absolute; left: 0; top: 0; width: 1200px; height: 702px; background: var(--stage-dark); }
  .stage__title {
    position: absolute; top: 50px; left: 0; width: 100%; text-align: center;
    font-family: "Montserrat", sans-serif; font-weight: 600; font-size: 31px;
    letter-spacing: 1.5px; color: var(--stage-title);
  }

  /* Billboard artwork */
  .billboard {
    position: absolute; width: 1090px; height: 515px; overflow: hidden;
    background: var(--sheet-white); border: 1px solid #8a8a8a;
  }
  .billboard--main { left: 60px; top: 144px; }
  .billboard--mini { left: 94px; top: 798px; transform: scale(0.4358); transform-origin: 0 0; border-width: 2px; }

  .billboard__photo {
    position: absolute; left: 420px; top: 0; width: 670px; height: 515px;
    background:
      linear-gradient(90deg, #ffffff 0%, rgba(255,255,255,0.85) 22%, rgba(255,255,255,0) 55%),
      radial-gradient(ellipse at 72% 40%, #f0c9a8 0%, #e3ad88 14%, rgba(227,173,136,0) 26%),
      linear-gradient(160deg, #f3f6f8 0%, #dfe9ef 35%, #6fa4d6 62%, #2f6fb8 78%, #1f4a6e 100%);
  }
  .billboard__headline { position: absolute; left: 67px; top: 48px; }
  .headline__lead {
    display: block; font-weight: 700; font-size: 46px; color: var(--headline-blue); line-height: 56px;
  }
  .headline__main {
    display: block; margin-left: 37px; font-weight: 700; font-size: 48px;
    color: var(--headline-navy); line-height: 58px; letter-spacing: 0.5px;
  }
  .billboard__phone {
    position: absolute; left: 81px; top: 236px; height: 68px; display: flex; align-items: center; gap: 22px;
    font-weight: 500; font-size: 56px; line-height: 68px; letter-spacing: 3px; color: var(--phone-teal);
  }
  .billboard__phone svg { width: 44px; height: 44px; flex: none; }
  .billboard__brand { position: absolute; left: 45px; top: 390px; height: 64px; display: flex; align-items: center; gap: 12px; }
  .brand__mark { width: 56px; height: 56px; border-radius: 50%; background: var(--brand-teal); flex: none; }
  .brand__text { display: flex; flex-direction: column; align-items: flex-end; }
  .brand__name { font-weight: 500; font-size: 32px; color: var(--brand-teal); line-height: 38px; }
  .brand__tagline { font-weight: 400; font-size: 16px; line-height: 20px; color: var(--brand-blue); }
  .billboard__address {
    position: absolute; left: 50px; top: 480px; font-size: 16px; line-height: 22px; color: var(--body-grey);
  }

  /* Display dimensions */
  .dimensions__title {
    position: absolute; left: 94px; top: 736px; width: 474px; text-align: center;
    font-family: "Jost", sans-serif; font-weight: 500; font-size: 27px; color: var(--spec-blue);
  }
  .dimensions__width { position: absolute; left: 94px; top: 772px; width: 474px; height: 20px; }
  .dimensions__width::before {
    content: ""; position: absolute; left: 0; right: 0; top: 10px; border-top: 2px solid var(--rule);
  }
  .dimensions__width span, .dimensions__height span {
    position: relative; background: var(--sheet-white); font-family: "Jost", sans-serif;
    font-weight: 500; font-size: 17px; color: var(--rule); padding: 0 6px;
  }
  .dimensions__width span { display: block; width: 76px; margin: 0 auto; text-align: center; }
  .dimensions__height { position: absolute; left: 34px; top: 798px; width: 56px; height: 226px; }
  .dimensions__height::before {
    content: ""; position: absolute; left: 44px; top: 0; bottom: 0; border-left: 2px solid var(--rule);
  }
  .dimensions__height span { position: absolute; left: 0; top: 104px; padding: 2px 0; }

  /* Content specifications */
  .specs { position: absolute; left: 641px; top: 770px; font-family: "Jost", sans-serif; }
  .specs__title { font-weight: 500; font-size: 24px; color: var(--spec-blue); margin-bottom: 10px; }
  .specs__list { list-style: none; }
  .specs__list li {
    position: relative; padding-left: 20px; font-size: 15.5px; line-height: 25px; color: var(--spec-grey);
  }
  .specs__list li::before {
    content: ""; position: absolute; left: 4px; top: 11px; width: 5px; height: 5px;
    border-radius: 50%; background: var(--spec-grey);
  }
</style>
</head>
<body>

<section class="stage">
  <h1 class="stage__title">REVISED DESIGN (216x456 pixels)</h1>

  <div class="billboard billboard--main">
    <div class="billboard__photo" role="img" aria-label="Smiling young boy in a dental chair wearing a blue bib, with a dentist's gloved hand holding a mirror"></div>
    <h2 class="billboard__headline">
      <span class="headline__lead">We Love Kids and Know</span>
      <span class="headline__main">HOW TO CARE FOR THEM</span>
    </h2>
    <div class="billboard__phone">
      <svg viewBox="0 0 24 24" aria-hidden="true"><path fill="none" stroke="#1f5a50" stroke-width="2.2" stroke-linejoin="round" d="M6.5 2.5l3 4-2 2.5c1 2.5 3 4.5 5.5 5.5l2.5-2 4 3-2 4c-8 0-15-7-15-15z"/><circle cx="12" cy="12" r="10.5" fill="none" stroke="#1f5a50" stroke-width="1.6"/></svg>
      <span>555 014 2368</span>
    </div>
    <div class="billboard__brand">
      <span class="brand__mark"></span>
      <div class="brand__text">
        <span class="brand__name">Maple Cove Dental</span>
        <span class="brand__tagline">general dentistry for children</span>
      </div>
    </div>
    <p class="billboard__address">ADDRESS: 48 W Birchwood</p>
  </div>
</section>

<section class="dimensions">
  <h3 class="dimensions__title">DISPLAY DIMENSIONS</h3>
  <div class="dimensions__width"><span>456(w)</span></div>
  <div class="dimensions__height"><span>216(h)</span></div>

  <div class="billboard billboard--mini">
    <div class="billboard__photo" role="img" aria-label="Smiling young boy in a dental chair wearing a blue bib"></div>
    <h2 class="billboard__headline">
      <span class="headline__lead">We Love Kids and Know</span>
      <span class="headline__main">HOW TO CARE FOR THEM</span>
    </h2>
    <div class="billboard__phone">
      <svg viewBox="0 0 24 24" aria-hidden="true"><path fill="none" stroke="#1f5a50" stroke-width="2.2" stroke-linejoin="round" d="M6.5 2.5l3 4-2 2.5c1 2.5 3 4.5 5.5 5.5l2.5-2 4 3-2 4c-8 0-15-7-15-15z"/><circle cx="12" cy="12" r="10.5" fill="none" stroke="#1f5a50" stroke-width="1.6"/></svg>
      <span>555 014 2368</span>
    </div>
    <div class="billboard__brand">
      <span class="brand__mark"></span>
      <div class="brand__text">
        <span class="brand__name">Maple Cove Dental</span>
        <span class="brand__tagline">general dentistry for children</span>
      </div>
    </div>
    <p class="billboard__address">ADDRESS: 48 W Birchwood</p>
  </div>
</section>

<section class="specs">
  <h3 class="specs__title">CONTENT SPECIFICATIONS</h3>
  <ul class="specs__list">
    <li>Composition size: 456 pixels (w) by 216 pixels (h)</li>
    <li>Color mode: RGB</li>
    <li>Resolution: 72 dpi (use high-resolution assets and/or vector graphics)</li>
    <li>Preferred Static file format: PNG</li>
    <li>Supported Static file formats: BMP, JPEG</li>
    <li>Pixel aspect ratio: square pixels</li>
    <li>Preferred Animated file format: AVI (uncompressed)</li>
    <li>Supported Animated file formats: MP4, MOV</li>
    <li>Frames Per Second: 30</li>
  </ul>
</section>

</body>
</html>
```